packaging design for disposable trash bag

We need 3 design for 3 of our products. first item is trash bag,the second item is disposable table cover and third is food packaging bag . We are a company in Singapore selling disposable product. This packaging products will be sold on shelf or online.

Attached is the requirement of the product. And some samples.
Updates

Target Market(s)

adult, most likely housewife

Requirements
Must have
• Packing design requirement for trash bag
• 1. Include company logo design, which is attached in the creative brief. MIRVALE POLYPAK.
• 2. Clear showing of the product and its illustration of using. Eg. The trash bin.
• 3. Allocate a box for the purpose of sticking product size sticker.
• 4. Each packing bag holds 10pcs
• 5. Show of country of origin. Product of Singapore.
• 6. Use of one colour for printing of packing bag ( Black / blue/ bright Green/ white )
• 7. Show of warning: Keep polythene bags away from young children
• 8. dimension of the packagaing printing area : Lenght : 20 cm , Height 26 cm
• Packing design requirement for disposable Table Cover
• 1. Include company logo design, which is attached in the creative brief. Our company is MIRVALE POLYPAK.
• 2. Clear showing of the product and its illustration of using. Eg. The table?.
• 4. Each packing bag holds 5pcs
• 6. Use of one colour for printing of the packing bag ( Black / blue/ bright Green )
• Packing design requirement for disposable food packaging plastic bag
• 2. Clear showing of the product and its illustration of using. Eg. Food?.
• 4. Show of country of origin. Product of Singapore.
• 5. Use of one colour for printing of the packing bag ( Black/ bright green )
• 6. Show of warning: Keep polythene bags away from young children
• 7. Show of product information: hygienic, food grade, freezer resistance, grease proof, damp proof, heat resistant.
• 8. Include the open here packing opening.
• 9. dimension of the packagaing printing area : Lenght : 15 cm , Height 22 cm
Nice to have
• requirement is stated in the must have. Good to allocate some space beside the packaging PCS area for promotion stickers . And also space allocated for bar code stickers.
Should not have
• no more than one color for printing

```html
<!DOCTYPE html>
<html lang="en">
<head>
<meta charset="utf-8">
<title>Mirvale Polypak – Disposable Table Cover Packaging</title>
<link rel="stylesheet" href="https://fonts.googleapis.com/css2?family=Oswald:wght@200;300;400;500;600&display=swap">
<style>
  :root {
    --print-blue: #1d9fe0;
    --brand-green: #2ea84d;
    --bg-light: #ececec;
    --bg-mid: #a9a9a9;
    --bg-dark: #4f4f4f;
    --cover-light: rgba(236, 236, 236, 0.55);
    --cover-edge: rgba(29, 159, 224, 0.22);
    --icon-tint: rgba(29, 159, 224, 0.28);
  }
  * { margin: 0; padding: 0; box-sizing: border-box; }
  html, body { width: 801px; height: 1200px; overflow: hidden; background: var(--bg-dark); }
  .pack {
    position: relative;
    width: 801px;
    height: 1200px;
    overflow: hidden;
    background: radial-gradient(ellipse 62% 58% at 50% 52%, var(--bg-light) 0%, var(--bg-mid) 62%, var(--bg-dark) 100%);
    font-family: "Oswald", "Arial Narrow", sans-serif;
    color: var(--print-blue);
  }
  .brand {
    position: absolute;
    top: 66px;
    left: 0;
    width: 100%;
    text-align: center;
    color: var(--brand-green);
    font-weight: 400;
    font-size: 18px;
    line-height: 16px;
    letter-spacing: 0.3px;
  }
  .brand-square {
    display: block;
    width: 32px;
    height: 32px;
    margin: 0 auto 14px;
    background: var(--brand-green);
  }
  .product-illustration {
    position: absolute;
    top: 0;
    left: 0;
  }
  .product-name {
    position: absolute;
    left: 0;
    width: 100%;
    text-align: center;
    line-height: 1;
    text-transform: uppercase;
    white-space: nowrap;
  }
  .product-name--light { top: 232px; font-size: 82px; font-weight: 300; padding-left: 4px; }
  .product-name--bold { top: 331px; font-size: 86px; font-weight: 500; letter-spacing: -1px; padding-left: 30px; }
  .size-box {
    position: absolute;
    left: 293px;
    top: 508px;
    width: 214px;
    height: 177px;
    border-top: 3px solid var(--print-blue);
    border-bottom: 3px solid var(--print-blue);
  }
  .size-label {
    position: absolute;
    top: 4px;
    left: 78px;
    font-size: 33px;
    font-weight: 600;
    line-height: 1;
  }
  .pack-count {
    position: absolute;
    left: 176px;
    top: 770px;
    line-height: 1;
    white-space: nowrap;
  }
  .pack-count-number { font-size: 128px; font-weight: 400; }
  .pack-count-unit { font-size: 72px; font-weight: 200; vertical-align: 40px; margin-left: 10px; }
  .origin {
    position: absolute;
    left: 0;
    width: 100%;
    text-align: center;
    line-height: 1;
  }
  .origin--material { top: 1015px; font-size: 19px; font-weight: 600; }
  .origin--country { top: 1042px; font-size: 24px; font-weight: 400; }
  .warning {
    position: absolute;
    top: 1113px;
    left: 0;
    width: 100%;
    text-align: center;
    font-size: 16px;
    font-weight: 300;
    letter-spacing: 0.5px;
    word-spacing: 5px;
  }
  .warning-label { font-weight: 600; }
  .icon-placeholder { position: absolute; }
</style>
</head>
<body>
<main class="pack">
  <header class="brand">
    <span class="brand-square"></span>
    MIRVALE POLYPAK<br>PTE LTD
  </header>

  <svg class="product-illustration" width="801" height="1200" viewBox="0 0 801 1200" role="img" aria-label="Line illustration of a round pedestal table draped with a disposable table cover">
    <defs>
      <radialGradient id="coverFill" cx="0.5" cy="0.45" r="0.7">
        <stop offset="0" stop-color="var(--cover-light)"/>
        <stop offset="1" stop-color="var(--cover-edge)"/>
      </radialGradient>
    </defs>
    <rect x="62" y="176" width="684" height="744" rx="18" fill="url(#coverFill)"/>
  </svg>

  <h1>
    <span class="product-name product-name--light">Disposable</span>
    <span class="product-name product-name--bold">Table Cover</span>
  </h1>

  <div class="size-box">
    <span class="size-label">SIZE:</span>
  </div>

  <p class="pack-count"><span class="pack-count-number">5</span><span class="pack-count-unit">PCS</span></p>

  <svg class="icon-placeholder" style="left:124px;top:934px" width="112" height="138" role="img" aria-label="Dispose in bin icon">
    <rect width="112" height="138" rx="6" fill="var(--icon-tint)"/>
  </svg>

  <svg class="icon-placeholder" style="left:595px;top:974px" width="106" height="102" role="img" aria-label="Recycling symbol">
    <rect width="106" height="102" rx="6" fill="var(--icon-tint)"/>
  </svg>

  <p class="origin origin--material">100% RECYKLED MATERIALS</p>
  <p class="origin origin--country">PRODUCT OF SINGAPORE</p>

  <p class="warning"><span class="warning-label">WARNING:</span> KEEP POLYTHENE BAGS AWAY FROM YOUNG CHILDREN</p>
</main>
</body>
</html>
```